Re-launching marine insurance adjusting company - looking for energy

I am a sole practitioner specializing in the profession of average adjusting. There is an on-line brochure at www.kbrtmarine.example I am one of only a handful of specialists in this field and I enjoy a fair amount of name recognition, domestically in the US and internationally. My principal markets are the US, the London and Scandinavian insurance markets and shipowners and insurers in Latin America.
The business is a mixture of law, accounting and insurance and my clientele relies on a time-sensitive and accurate work-product, clearly stating an insurance company's liability for a given claim. The identity needs to project gravitas rather than flash.
Since 1998 I have traded as "The Halloway Bureau" but have also attempted to establish the name KBRTMARINE.example so that people would visit my website.
I want to implement a single identity across my stationery, business cards and website. I have come to see "The Halloway Bureau" as rather fatuous, since there is no company, it is just me. The Internet domain KBRTMARINE is long-established and I would be reluctant to change it. I have considered trading as simply Marcus T Holloway, MTH, KBRTMARINE or attempting to come up with a name that could be abbreviated to MTH, e.g. M Holloway Tessellate - but I can't find a suitable word for the second S.
Logo-wise, I have considered a stylized MTH or KBRTMARINE redolent of waves of the sea. A nautical theme embodying a cargo ship, navigational beacon or lighthouse might be appropriate but these tend to be hackneyed.
I have attached a card that I mocked up at Zib, connoting stacking up numbers, which I really like, but I think it is too cryptic for people in most insurance companies, who don't particularly think laterally or they wouldn't work in marine insurance, and the card that I use currently, which I intended to be understated, but in fact it states nothing.
I have also attached my current letterhead, to demonstrate how I really need help.
Finally, I have attached a credentials sheet, to attempt to establish how narrow and deep is the professional niche that I occupy.
What I am looking to implement is a single logo, font, them and color scheme to use across my website, letterhead and business cards.
Over to the Pencil Guild...
Ship owners and insurance companies
Accounting

```html
<!DOCTYPE html>
<html lang="en">
<head>
<meta charset="utf-8">
<title>KBRTMARINE Letterhead</title>
<link rel="stylesheet" href="https://fonts.googleapis.com/css2?family=Montserrat:wght@400;500;600&display=swap">
<style>
  :root {
    --backdrop: #939498;
    --paper: #ffffff;
    --sky: #33a4dd;
    --navy: #27347c;
    --text: #2b2b2b;
  }
  * { margin: 0; padding: 0; box-sizing: border-box; }
  html, body {
    width: 1200px; height: 1000px; overflow: hidden;
    background: var(--backdrop);
    font-family: "Montserrat", sans-serif;
  }
  .letterhead {
    position: absolute; left: 300px; top: 76px;
    width: 600px; height: 848px;
    background: var(--paper);
    box-shadow: 0 4px 14px rgba(0,0,0,0.25);
    overflow: hidden;
  }
  .side-wave { position: absolute; inset: 0; width: 100%; height: 100%; }
  .brand {
    position: absolute; top: 72px; right: 44px;
    display: flex; align-items: center; gap: 10px;
    color: var(--navy); font-weight: 600; font-size: 22px; letter-spacing: 1px;
  }
  .brand-dot { width: 14px; height: 14px; border-radius: 50%; background: var(--sky); }
  .contact-bar {
    position: absolute; left: 120px; right: 20px; bottom: 52px;
    font-size: 9px; color: var(--text);
  }
  .contact-list {
    list-style: none; display: flex; gap: 18px; justify-content: center;
    flex-wrap: nowrap;
  }
  .contact-list li {
    display: flex; align-items: center; gap: 5px;
    white-space: nowrap;
  }
  .contact-icon {
    width: 11px; height: 11px; flex-shrink: 0;
    fill: var(--navy);
  }
  .address { text-align: center; margin-top: 8px; font-size: 9.5px; white-space: nowrap; }
</style>
</head>
<body>
  <main class="letterhead">
    <svg class="side-wave" viewBox="0 0 600 848" aria-hidden="true">
      <path fill="var(--navy)" d="M0 0 H160 C100 40 74 150 78 270 C82 420 70 620 48 848 H0 Z"/>
      <path fill="var(--sky)" d="M0 0 H118 C70 40 56 150 58 270 C61 420 48 620 20 848 H0 Z"/>
      <path fill="none" stroke="#ffffff" stroke-width="2" d="M118 0 C70 40 56 150 58 270 C61 420 48 620 20 848"/>
    </svg>

    <div class="brand">
      <span class="brand-dot"></span>
      <span class="brand-name">KBRTMARINE</span>
    </div>

    <footer class="contact-bar">
      <ul class="contact-list">
        <li><svg class="contact-icon" viewBox="0 0 10 10"><path d="M2 1 L4 1 L4.5 3 L3.3 4 C4 5.5 4.5 6 6 6.7 L7 5.5 L9 6 L9 8 C5 9 1 5 2 1 Z"/></svg>(212) 555 0147</li>
        <li><svg class="contact-icon" viewBox="0 0 10 10"><rect x="1" y="4" width="8" height="5" rx="1"/><rect x="3" y="1" width="4" height="3"/></svg>(212) 555 0193</li>
        <li><svg class="contact-icon" viewBox="0 0 10 10"><path d="M1 2 H9 V8 H1 Z M1.8 2.8 L5 5.2 L8.2 2.8" /></svg>info@kbrtmarine.example</li>
        <li><svg class="contact-icon" viewBox="0 0 10 10"><circle cx="5" cy="5" r="4"/></svg>www.kbrtmarine.example</li>
      </ul>
      <p class="address">48 Harbor View Lane, New York, NY 10099, USA</p>
    </footer>
  </main>
</body>
</html>
```